Exciting adult social quiz app needs awesome modern design

A new and exciting app for couples/sexual partners is in the making. It will be available for Korvix and Plume devices and allow one partner to invite another partner to the game. The partners will answer questions about their sexual desires and needs and then try to guess what the other one answered.

The app needs a high quality design and you can find some general inspiration in a similar social quiz app called "Pair Riddle" which can be found in Vela Shop and Runa Market. I like some of the basic layouts of this app.

The design should be classy and have a theme that matches the app subject. This is a sexual get-to-know-each-other-app and not a "porn app". I imagine colors might be black and red (not a requirement) and perhaps have some structures, pictures or backgrounds showing a bit of skin. It's important that the game can be accessed by players in the public space (e.g. in a bus, car etc.) without surroundings thinking it's a sex/porn game - but also important that it's exciting in a kind of sexual way. So try to find a fine line.

As the app is for both genders, the design should accommodate this.

Please see app mockups in the attached PDF.

Initially, please show design proposals for screens 13, 16 and 23.
Please notice that screen 16 doesn't have to be exactly those 2 bars - please make some alternative score comparison graphic in your proposal.

Looking forward to seeing your proposal soon!

Target Market(s)

Couples between 18 and 50

Industry/Entity Type

Adult

Requirements
Must have
• Smooth graphics like the app "Pair Riddle"
Nice to have
• Several proposals are appreciated. Perhaps you can show your proposals with different colors and object placements so that I can see some different options.

```html
<!DOCTYPE html>
<html lang="en">
<head>
<meta charset="utf-8">
<title>Waiting for Your turn</title>
<link href="https://fonts.googleapis.com/css2?family=Arimo:ital,wght@0,400;0,700;1,400&display=swap" rel="stylesheet">
<style>
  :root {
    --ink: #111111;
    --name: #8a2f74;
    --nudge-bg: rgba(243, 196, 70, 0.82);
    --nudge-ink: #3a2a10;
    --panel: rgba(150, 195, 240, 0.55);
    --alert: #1f78d1;
    --reply: #f08a1c;
    --input-bg: rgba(225, 235, 245, 0.78);
    --input-ink: #7a8594;
    --heart: #d8202a;
    --photo-a: #e9e4e0;
    --photo-b: #d9b9a8;
    --photo-c: #8fb0cf;
    --photo-d: #c99a85;
    --photo-e: #efe6df;
  }
  * { box-sizing: border-box; margin: 0; padding: 0; }
  html, body { width: 674px; height: 1200px; overflow: hidden; background: #ffffff; }
  .screen {
    position: relative;
    width: 674px;
    height: 1200px;
    overflow: hidden;
    font-family: "Arimo", Arial, sans-serif;
  }
  .backdrop {
    position: absolute; inset: 0;
    background:
      radial-gradient(ellipse 45% 30% at 62% 10%, #d86a82 0%, rgba(216,106,130,0) 70%),
      radial-gradient(ellipse 40% 55% at 60% 48%, var(--photo-c) 0%, rgba(143,176,207,0) 75%),
      radial-gradient(ellipse 35% 45% at 88% 60%, var(--photo-d) 0%, rgba(201,154,133,0) 75%),
      linear-gradient(160deg, var(--photo-a) 0%, var(--photo-b) 40%, var(--photo-e) 100%);
  }
  .turn-title {
    position: absolute; top: 22px; left: 0; width: 100%;
    text-align: center; font-weight: 700; font-size: 34px; color: var(--ink);
  }
  .avatar {
    position: absolute; border-radius: 50%;
    border: 3px solid #c98a4a;
    background: radial-gradient(circle at 50% 40%, #f3c79c, #c56a3e);
  }
  .player-avatar { left: 30px; top: 82px; width: 86px; height: 86px; }
  .player-name {
    position: absolute; left: 30px; top: 224px; width: 86px;
    text-align: center; font-weight: 700; font-size: 26px; color: var(--name);
  }
  .nudge {
    position: absolute; left: 362px; top: 100px; width: 266px; height: 80px;
    background: var(--nudge-bg);
    display: flex; align-items: center; justify-content: center; gap: 10px;
    font-weight: 700; font-size: 29px; color: var(--nudge-ink);
  }
  .alert { position: absolute; left: 488px; top: 250px; width: 116px; height: 112px; }
  .chat-panel {
    position: absolute; left: 94px; top: 300px; width: 498px; height: 600px;
    background: var(--panel);
  }
  .message {
    position: absolute; left: 40px; display: flex; align-items: center; gap: 22px;
    font-weight: 700; font-size: 30px;
  }
  .message .avatar { position: static; width: 56px; height: 56px; border-width: 2px; }
  .message-first { top: 102px; color: var(--ink); }
  .message-second { top: 198px; color: var(--reply); }
  .message-second .avatar { background: radial-gradient(circle at 50% 40%, #c9a890, #6e4f40); border-color: #9b7b64; }
  .heart { position: absolute; left: 54px; top: 904px; width: 60px; height: 60px; }
  .chat-input {
    position: absolute; left: 140px; top: 926px; width: 452px; height: 90px;
    background: var(--input-bg); border-radius: 6px;
    display: flex; align-items: center; padding-left: 36px;
    font-style: italic; font-weight: 700; font-size: 28px; color: var(--input-ink);
  }
</style>
</head>
<body>
<main class="screen">
  <div class="backdrop" role="img" aria-label="Background photo of a tattooed woman with pink hair reading a magazine"></div>

  <h1 class="turn-title">Waiting for Your turn</h1>

  <div class="avatar player-avatar" role="img" aria-label="Profile photo of Laura"></div>
  <div class="player-name">Laura</div>

  <div class="nudge">
    <svg width="34" height="36" viewBox="0 0 34 36" aria-hidden="true">
      <path d="M17 3c-6 0-10 5-10 11v8l-4 5h28l-4-5v-8c0-6-4-11-10-11z" fill="#f5a623" stroke="#a0660f" stroke-width="2"/>
      <circle cx="17" cy="31" r="4" fill="#a0660f"/>
    </svg>
    <span>Send Nudge</span>
  </div>

  <svg class="alert" viewBox="0 0 116 112" aria-hidden="true">
    <path d="M58 6c28 0 50 18 50 42s-22 42-50 42c-5 0-10-1-14-2L14 106l8-26C12 71 8 60 8 48 8 24 30 6 58 6z" fill="var(--alert)" stroke="#ffffff" stroke-width="5"/>
    <rect x="51" y="22" width="14" height="38" rx="6" fill="#ffffff"/>
    <circle cx="58" cy="74" r="8" fill="#ffffff"/>
  </svg>

  <section class="chat-panel">
    <div class="message message-first">
      <div class="avatar" role="img" aria-label="Profile photo of Laura"></div>
      <span>We can chat here !</span>
    </div>
    <div class="message message-second">
      <div class="avatar" role="img" aria-label="Profile photo of the partner"></div>
      <span>Cool !</span>
    </div>
  </section>

  <svg class="heart" viewBox="0 0 60 60" aria-hidden="true">
    <path d="M30 54C10 38 4 30 4 20 4 11 11 5 19 5c5 0 9 3 11 7 2-4 6-7 11-7 8 0 15 6 15 15 0 10-6 18-26 34z" fill="var(--heart)" stroke="#ffffff" stroke-width="3"/>
    <circle cx="30" cy="27" r="8" fill="#2a0a0a"/>
  </svg>
  <div class="chat-input">Chat text here...</div>
</main>
</body>
</html>
```